Cause bitches need love too!

I am creating an ad campaign. It will be a series of featured dogs in our shelter and they will contain a picture of the dog wich should be big enough to see on a yard sign and will change every week. I am placing the signs so that they lead you to the shelter. This is why I am also including the copy that says "you're almost there".

I have 4 tag lines:

1. Find unconditional Love.
2. She'll Love you furever!
3. He'll always listen.
4. Meet your new BFF

You're almost there 318 W Harrowgate Ln
Open 10 - 7/Tues-Sat

The dimensions for the sign are 24" wide and 18" high

Every week we will have a different picture of a different dog (hopefully last week's dog gets adopted). Anyhow, I am printing out yard signs, meaning that instead of printing 160 different signs it would be ideal just to replace the photo. So far the copy that is permanent is: "You're almost there. 318 W. Harrowgate Ln."

I could silhouette the image of the dog as well and super impose it on the sign, that's also a consideration, but ideally if I could have 4 tag lines I could print 40 signs of each and just replace the photo manually each week from my printer that would save costs.
Updates

Not enough designs to chose from and I edited the brief and committed to pay no matter what to increase the amount of designs as per your suggestions.

Target Market(s)

Animal lovers

Industry/Entity Type

Campaign

Font styles to use
Sans Serif

Colors

Designer to choose colors to be used in the design.

Requirements
Must have
• The dimensions for the sign are 24" wide and 18" high
Nice to have
• I want the signs to be hip, they should have a positive feel to them. You can alter the photos if you like. I am even open to new copy if you think something else works better.

```html
<!DOCTYPE html>
<html lang="en">
<head>
<meta charset="utf-8">
<title>She'll Love You Furever – Yard Sign</title>
<link href="https://fonts.googleapis.com/css2?family=Bebas+Neue&family=Lato:wght@400;700&display=swap" rel="stylesheet">
<style>
  :root {
    --page-bg: #5a5a5a;
    --navy: #2f4597;
    --navy-light: #4a5fae;
    --cyan: #35c6e6;
    --yellow: #fde232;
    --white: #ffffff;
    --ink: #333333;
    --photo-grey: #d6d2d0;
    --photo-grey-dark: #b9b5b3;
    --photo-tan: #b88a4e;
  }
  html, body {
    margin: 0;
    width: 1200px;
    height: 1200px;
    overflow: hidden;
    background: var(--page-bg);
  }
  .yard-sign {
    position: absolute;
    left: 60px;
    top: 195px;
    width: 1080px;
    height: 810px;
    box-shadow: 0 10px 30px rgba(0,0,0,0.35);
  }
  .yard-sign svg { display: block; width: 100%; height: 100%; }
  .headline {
    font-family: "Bebas Neue", "Oswald", sans-serif;
    font-size: 140px;
  }
  .headline-cyan { fill: var(--cyan); }
  .headline-yellow { fill: var(--yellow); }
  .subline {
    font-family: "Lato", sans-serif;
    font-weight: 700;
    font-size: 38px;
    fill: var(--yellow);
  }
  .address {
    font-family: "Lato", sans-serif;
    font-weight: 400;
    font-size: 40px;
    fill: var(--ink);
  }
  .pin { fill: var(--navy); }
</style>
</head>
<body>
  <div class="yard-sign">
    <svg viewBox="0 0 1200 900" xmlns="http://www.w3.org/2000/svg">
      <defs>
        <radialGradient id="faint-dog-tone" cx="0.45" cy="0.35" r="0.6">
          <stop offset="0" stop-color="var(--navy-light)"/>
          <stop offset="1" stop-color="var(--navy)"/>
        </radialGradient>
        <radialGradient id="featured-dog-tone" cx="0.55" cy="0.55" r="0.6">
          <stop offset="0" stop-color="var(--photo-tan)"/>
          <stop offset="0.55" stop-color="var(--photo-grey-dark)"/>
          <stop offset="1" stop-color="var(--photo-grey)"/>
        </radialGradient>
        <clipPath id="sign-bounds">
          <rect x="0" y="0" width="1200" height="900"/>
        </clipPath>
      </defs>

      <g clip-path="url(#sign-bounds)">
        <!-- navy field -->
        <rect class="navy-field" x="0" y="0" width="1200" height="900" fill="var(--navy)"/>
        <rect class="background-dog" x="20" y="60" width="640" height="760" fill="url(#faint-dog-tone)"
              role="img" aria-label="Faint blue-toned close-up of a shelter dog's face"/>

        <!-- address band -->
        <rect class="address-band" x="0" y="812" width="1200" height="88" fill="var(--white)"/>

        <!-- arc bands framing the featured dog -->
        <circle class="arc-cyan" cx="1085" cy="460" r="590" fill="var(--cyan)"/>
        <circle class="arc-yellow" cx="1085" cy="460" r="562" fill="var(--yellow)"/>
        <circle class="arc-white" cx="1085" cy="460" r="548" fill="var(--white)"/>
        <circle class="featured-dog" cx="1085" cy="460" r="535" fill="url(#featured-dog-tone)"
                role="img" aria-label="Photo of this week's featured shelter dog, a tan and black mixed breed"/>
      </g>

      <!-- tagline -->
      <text class="headline headline-cyan" x="60" y="290">SHE'LL</text>
      <text class="headline headline-yellow" x="60" y="457">LOVE YOU</text>
      <text class="headline headline-cyan" x="60" y="625">FUREVER!</text>

      <text class="subline" x="83" y="785">You're almost there.</text>

      <!-- location -->
      <g class="pin" transform="translate(103 850)">
        <path d="M0 -22 C-12 -22 -18 -13 -18 -5 C-18 7 0 22 0 22 C0 22 18 7 18 -5 C18 -13 12 -22 0 -22 Z M0 -11 A6 6 0 1 0 0.01 -11 Z" fill-rule="evenodd"/>
        <circle cx="0" cy="-5" r="6" fill="var(--white)"/>
      </g>
      <text class="address" x="145" y="862">318 W. Harrowgate Ln.</text>
    </svg>
  </div>
</body>
</html>
```